Pilates business needs a face list flyer

We are a pilates business that has been based in England for 15 years and looking for a new flyer that is eye catch and modern but stylish
we are trying to capture the male market as well as the female market so the leaflet should draw attention to both groups.
I have attached a copy of the literature needed on the flyer also a picture of its founder

Target Market(s)

market age group 18-70+ male and female

Industry/Entity Type

Business

Font styles to use
Other font styles liked:
• calbri

Colors
33b8a4
34a7d8
3277b5
abd037

Requirements
Must have
• Literature attached
Nice to have
• To target both the male and female market. stylish but eye catching
Should not have
• pinks purples

```html
<!DOCTYPE html>
<html lang="en">
<head>
<meta charset="UTF-8">
<title>Pilates Flyer</title>
<link rel="stylesheet" href="https://fonts.googleapis.com/css2?family=Carlito:wght@400;700&family=Open+Sans:wght@400;600;700&display=swap">
<style>
  :root {
    --navy: #0f3142;
    --navy-deep: #0a2331;
    --teal: #33b8a4;
    --sky: #34a7d8;
    --blue: #3277b5;
    --lime: #abd037;
    --ink: #2f3a40;
    --paper: #ffffff;
    --mist: #eef3f4;
  }
  * { margin: 0; padding: 0; box-sizing: border-box; }
  html, body { width: 900px; height: 1200px; overflow: hidden; background: var(--paper); }
  .flyer {
    position: relative;
    width: 900px; height: 1200px;
    overflow: hidden;
    font-family: "Carlito", "Open Sans", sans-serif;
    color: var(--ink);
  }
  .backdrop { position: absolute; inset: 0; }
  .intro {
    position: absolute; left: 60px; top: 30px; width: 790px;
    color: #e6eff2;
  }
  .intro h2 {
    font-family: "Open Sans", sans-serif;
    font-weight: 700; font-size: 30px; color: var(--lime);
    margin-bottom: 8px;
  }
  .intro h3 {
    font-family: "Open Sans", sans-serif;
    font-weight: 700; font-size: 26px; color: #ffffff;
    margin: 22px 0 8px;
  }
  .intro p { font-size: 16px; line-height: 1.42; }
  .intro .classes-text { width: 480px; }
  .benefits {
    position: absolute; left: 592px; top: 398px; width: 290px;
    list-style: none;
  }
  .benefits li {
    position: relative; padding-left: 18px;
    font-size: 14px; line-height: 1.3; color: var(--ink);
    margin-bottom: 3px;
  }
  .benefits li::before {
    content: ""; position: absolute; left: 1px; top: 5px;
    width: 8px; height: 8px; border-radius: 50%; background: var(--lime);
  }
  .portrait {
    position: absolute; left: 545px; top: 640px;
    width: 330px; height: 330px; border-radius: 50%;
    background: radial-gradient(circle at 50% 40%, #c9c2b5 0%, #8d8a83 55%, #5f646a 100%);
    border: 9px solid #ffffff;
  }
  .descriptions {
    position: absolute; left: 60px; top: 478px; width: 410px;
  }
  .descriptions h2 {
    font-family: "Open Sans", sans-serif;
    font-weight: 600; font-size: 42px; color: var(--teal);
    margin-bottom: 12px; letter-spacing: -0.5px;
  }
  .class-item { margin-bottom: 18px; }
  .class-item h3 {
    font-family: "Open Sans", sans-serif;
    font-weight: 600; font-size: 26px; color: var(--teal);
    display: flex; align-items: center; gap: 10px; margin-bottom: 6px;
  }
  .class-item h3::before {
    content: ""; width: 15px; height: 15px; border-radius: 50%;
    background: var(--lime); flex: none;
  }
  .class-item p { font-size: 16px; line-height: 1.4; color: var(--ink); }
  .class-item.wide p { width: 440px; }
</style>
</head>
<body>
<div class="flyer">
  <svg class="backdrop" width="900" height="1200" viewBox="0 0 900 1200" aria-hidden="true">
    <defs>
      <linearGradient id="band" x1="0" y1="0" x2="1" y2="1">
        <stop offset="0" stop-color="#144256"/>
        <stop offset="1" stop-color="#0a2331"/>
      </linearGradient>
    </defs>
    <rect width="900" height="1200" fill="#ffffff"/>
    <path d="M0 0 H900 V330 C760 360 560 360 420 400 C260 440 120 430 0 410 Z" fill="url(#band)"/>
    <path d="M0 410 C120 430 260 440 420 400 C330 450 180 470 0 460 Z" fill="#33b8a4"/>
    <circle cx="795" cy="655" r="350" fill="#abd037"/>
    <circle cx="810" cy="655" r="322" fill="#eef3f4"/>
    <path d="M900 1040 C820 1120 700 1170 560 1200 H900 Z" fill="#3277b5"/>
    <path d="M900 980 C840 1060 760 1110 640 1150 C740 1150 840 1110 900 1060 Z" fill="#34a7d8"/>
  </svg>

  <section class="intro">
    <h2>What is Pilates?</h2>
    <p>Pilates is now the hottest and most talked about fitness trend since the aerobic explosion of the past 30 years. A perfect blend of Eastern and Western philosophy, Pilates is a holistic approach to exercise that integrates body and mind. It concentrates on building strength, stamina, balance and co-ordination, improving flexibility, coordination, posture, breathing and well-being.</p>
    <h3>Classes</h3>
    <p class="classes-text">All classes are based upon the original 34 movements developed by the method's founder. Classes provide you with a safe yet highly intense workout, ideal for every age, whatever your ability or whether the individual is fit, sedentary or recuperating after illness or surgery. Furthermore, Pilates provides a safe and beneficial workout for expectant and new mothers.<br>Each session is designed to:</p>
  </section>

  <ul class="benefits">
    <li>Change the way you look</li>
    <li>Create lean muscles</li>
    <li>Increase strength, flexibility, coordination and proper body alignment</li>
    <li>Increase core strength</li>
    <li>Reduce fatigue, stress and risk of injury</li>
    <li>Reduce back and joint pain</li>
    <li>Rehabilitation</li>
    <li>Increase circulation</li>
    <li>Improve body mind integration</li>
  </ul>

  <div class="portrait" role="img" aria-label="Portrait photograph of the studio founder"></div>

  <section class="descriptions">
    <h2>Class Description</h2>
    <div class="class-item">
      <h3>Small Group Pilates (new)</h3>
      <p>This class is Structure similar to a private session. Max of 6 people allows movement plans to be more tailored to individual's needs than a larger group class. Will take from the basics and help to build on those skills to improve posture and to develop strength and flexibility. Home plan provided</p>
    </div>
    <div class="class-item">
      <h3>Beginner-Improvers</h3>
      <p>Ideal for those new to the Pilates technique. In this programme you will develop an understanding of the principals, gain strength, stamina and flexibility safely, as you are guided through a series of beginner movements, modified and tailored to your own needs and ability</p>
    </div>
    <div class="class-item wide">
      <h3>Progressive</h3>
      <p>Ideal stepping stone from beginners building on moves that you have already learnt at a more intense level, as well as learning new moves. Incorporating small equipment such as the toning ball, the stability ball, roller and Pilates balance weights to help increase the intensity of the workout without it being over challenging for those still developing their skill base.</p>
    </div>
  </section>
</div>
</body>
</html>
```